ホームページのデザイン作成をお願いします。
これまでのホームページとは違った印象のデザインを募集しています。
コーディングの必要はありません。

大まかなデザインは添付しておりますので、ご確認下さい。
パソコン、スマートフォン両用ページとなります。
添付画像とは別に、サイト構成として参考にしていただきたいものが
https://studio-mebelo.com/
になります。

1ページ完結型で、カテゴリー欄(店内の様子、猫紹介、システム、Q&A、SNS)
が横一列でありクリックをしたら、スクロールダウンするイメージです。

カテゴリー一覧
店内の様子、猫紹介、システム、Q&A、SNS
(添付参照)

参考内容
店内様子
→画像を数枚埋め込む予定

猫紹介
→横一列に並べ(表示は4匹程)、横にスクロールすれば他の猫がみれる形を予定しています。

システム
→表示させたいのは、添付画像の料金、猫のおやつ、営業時間となります。

Q&A
→ボタンを押したら下に広がるようになります

ルール
→猫のイラストは現在の画像を使用予定です

アクセス
→Googleマップ埋め込み+住所記載予定

SNS
→クリックで各ページに飛びます
ページ数
1ページ
希望イメージ
シンプル 複雑
単色 カラフル
暗い 明るい
日常 高級
遊び心 厳粛
未来的 伝統的
女性的 男性的
希望する色
黄・オレンジ系

男性ターゲットかつアキバの癒し空間というコンセプトの二点を融合させたイメージに一番近かったのでこちらを選定させて頂きました。
男性向けのデザインの中にもワンポイントで猫の可愛い要素が使われていた点が好評価に繋がりました。

皆様限られた抽象的なイメージのみの依頼で多数の提案を頂きましてありがとうございました。
難しいコンセプトでしたが非常に悩ましいデザインを提案して頂き、なんとか選定させて頂きました。
また機会がございましたら何卒よろしくお願い致します。

```html
<!DOCTYPE html>
<html lang="ja">
<head>
<meta charset="utf-8">
<title>猫ごよみ | 秋葉原の猫カフェ</title>
<link href="https://fonts.googleapis.com/css2?family=Noto+Sans+JP:wght@400;500;700&family=Kosugi+Maru&display=swap" rel="stylesheet">
<style>
:root{
  --orange:#f39a1e;
  --orange-deep:#e97c12;
  --orange-soft:#fbd48a;
  --peach:#fdebd6;
  --ink:#3a3330;
  --muted:#8b8580;
  --line:#e3ded8;
  --gray-bg:#eeeeee;
  --blue:#2b9ad8;
  --green:#39b54a;
  --dark:#2b2b2b;
  --white:#ffffff;
}
*{margin:0;padding:0;box-sizing:border-box}
html,body{width:1200px;height:4192px;overflow:hidden}
body{font-family:"Noto Sans JP",sans-serif;color:var(--ink);background:var(--white);font-size:13px;line-height:1.6}
.page{position:relative;width:1200px;height:4192px}
section,header,footer,nav{position:absolute;left:0;width:1200px}
.logo{font-family:"Kosugi Maru",sans-serif;font-weight:400;color:var(--ink);display:flex;align-items:baseline;gap:10px;white-space:nowrap}
.logo small{font-family:"Noto Sans JP",sans-serif;font-size:10px;color:var(--muted)}
.sec-title{text-align:center;font-size:13px;font-weight:400;color:var(--muted);letter-spacing:.2em;display:flex;align-items:center;justify-content:center;gap:16px}
.sec-title::before,.sec-title::after{content:"";width:60px;height:1px;background:var(--line)}
.ph{display:block;border-radius:2px}

/* header */
.site-header{top:0;height:64px;display:flex;align-items:center;justify-content:space-between;padding:0 120px}
.site-header .logo{font-size:26px}
.sns-mini{display:flex;gap:10px}
.sns-mini span{width:22px;height:22px;border-radius:4px;background:var(--orange)}
.sns-mini span:nth-child(2){background:#aaa}
.global-nav{top:64px;height:26px;background:var(--white)}
.global-nav ul{list-style:none;width:760px;height:26px;margin:0 auto;background:var(--orange);display:flex;justify-content:space-around;align-items:center}
.global-nav li{color:var(--white);font-size:11px;letter-spacing:.1em}

/* hero */
.hero{top:90px;height:390px;background:linear-gradient(100deg,#f6a623 0%,#f9c25a 45%,#ead8c4 70%,#c9b8a6 100%);overflow:hidden}
.hero .photo{position:absolute;right:0;top:0;width:640px;height:390px;background:radial-gradient(ellipse at 60% 55%,#d7c6b4 0%,#bba894 45%,rgba(240,170,60,0) 75%)}
.hero .badge{position:absolute;left:272px;top:20px;width:130px;height:130px;border-radius:50%;background:var(--orange-deep);color:var(--white);font-size:13px;font-weight:700;display:flex;align-items:center;justify-content:center;text-align:center;line-height:1.3;z-index:2}
.hero .title{position:absolute;left:330px;top:120px;width:330px;height:170px;background:rgba(255,255,255,.25);border:1px solid rgba(255,255,255,.7);color:var(--white);text-align:center;padding-top:18px}
.hero .title .logo{justify-content:center;color:var(--white);font-size:58px;line-height:1.1}
.hero .title em{font-style:normal;font-size:16px;letter-spacing:.25em;display:block;margin-top:6px}
.hero .lead{position:absolute;left:360px;top:300px;width:280px;text-align:center;color:var(--white);font-size:14px;font-weight:500;line-height:1.7}

/* concept */
.concept{top:480px;height:180px;padding-top:26px}
.concept .thumbs{display:flex;justify-content:center;gap:16px;margin-top:22px}
.concept .thumbs .ph{width:140px;height:96px}

/* intro band */
.intro{top:660px;height:140px;background:linear-gradient(90deg,#e8a640,#d9c57a 25%,#9fb27a 45%,#e6cc74 65%,#d98640 85%,#e7b267);display:flex;flex-direction:column;align-items:center;justify-content:center;color:var(--white)}
.intro h2{font-size:13px;font-weight:400;letter-spacing:.2em;margin-bottom:8px}
.intro p{font-size:12px;opacity:.9}

/* shop */
.shop{top:800px;height:300px;background:var(--gray-bg);padding-top:22px}
.shop .gallery{position:relative;width:560px;height:190px;margin:26px auto 0}
.shop .ph{position:absolute}

/* cats */
.cats{top:1100px;height:300px;padding-top:26px}
.cat-list{display:flex;justify-content:center;gap:18px;margin-top:40px}
.cat-card{width:150px;text-align:center}
.cat-card .ph{width:150px;height:150px}
.cat-card p{font-size:11px;color:var(--muted);margin-top:8px;letter-spacing:.1em}

/* system */
.system{top:1400px;height:560px;background:var(--gray-bg);padding-top:24px}
.price-list{width:900px;margin:24px auto 0;display:flex;flex-direction:column;gap:14px}
.price{background:var(--white);height:80px;display:flex;flex-direction:column;align-items:center;justify-content:center;box-shadow:0 1px 2px rgba(0,0,0,.08)}
.price strong{font-size:30px;font-weight:500;letter-spacing:.08em;line-height:1.3}
.price strong b{font-size:44px;font-weight:700}
.price strong small{font-size:13px}
.price span{font-size:10px;color:var(--muted)}
.price.snack strong{font-size:26px}
.price.hours{background:var(--orange-soft)}
.price.hours strong{color:var(--orange-deep)}
.system .note{text-align:center;font-size:11px;color:var(--muted);margin-top:26px}

/* qa */
.qa{top:1960px;height:460px;background:#fbf3e2;padding-top:24px}
.qa-list{width:600px;margin:26px auto 0;display:flex;flex-direction:column;gap:22px}
.qa-item h3{background:var(--blue);color:var(--white);font-size:12px;font-weight:500;padding:6px 16px;width:480px;border-radius:2px}
.qa-item p{font-size:12px;padding:10px 16px 0;line-height:1.8}
.qa-more{display:block;width:240px;margin:34px auto 0;background:var(--blue);color:var(--white);text-align:center;font-size:13px;padding:12px 0;border-radius:3px}
.qa-more::before{content:"＋";margin-right:10px;font-weight:700}

/* rules */
.rules{top:2420px;height:640px}
.rules-board{height:460px;background:var(--peach);padding-top:22px}
.rule-grid{position:relative;width:560px;height:380px;margin:20px auto 0}
.rule-card{position:absolute;width:130px;height:120px;background:var(--white);border-radius:6px;box-shadow:0 1px 3px rgba(0,0,0,.1);display:flex;flex-direction:column;align-items:center;justify-content:flex-end;padding-bottom:8px;font-size:12px;font-weight:700}
.rule-card .ph{width:90px;height:70px;margin-bottom:8px}
.rule-card.ng{color:#d23d2e}
.rule-intro{position:absolute;left:0;top:20px;width:130px;font-size:13px;font-weight:700;text-align:center}
.rule-intro .ph{width:90px;height:60px;margin:0 auto 8px;border-radius:50%}
.rules-text{width:840px;margin:22px auto 0;font-size:11px;line-height:2;color:var(--ink)}

/* access */
.access{top:3060px;height:350px;padding-top:22px}
.access-body{width:800px;margin:30px auto 0;display:flex;gap:30px}
.access-info{width:230px}
.access-info .logo{font-size:28px}
.access-info address{font-style:normal;font-size:11px;color:var(--muted);margin:6px 0 12px}
.access-info .ph{width:200px;height:150px}
.access .map{width:540px;height:250px}

/* sns */
.sns{top:3410px;height:350px;background:var(--peach);padding-top:22px}
.sns-list{display:flex;justify-content:center;gap:20px;margin-top:28px}
.sns-card{width:180px;height:250px;background:var(--orange);padding:10px;border-radius:3px}
.sns-card .inner{background:var(--white);height:100%;padding:10px;font-size:10px;color:var(--muted)}
.sns-card .inner .ph{height:90px;margin:8px 0}
.sns-card.talk{background:var(--green)}
.sns-card.talk .inner{text-align:center;color:var(--ink)}
.sns-card.talk .tag{color:var(--green);font-weight:700;font-size:14px;text-align:left}
.sns-card.talk .logo{justify-content:center;font-size:30px;margin:22px 0 4px}
.sns-card.talk .sub{font-size:11px;color:var(--muted);margin-bottom:8px}
.sns-card.talk .inner p{font-size:10px;color:#d23d2e}

/* company */
.company{top:3760px;height:320px;background:#f4f4f4;padding-top:20px}
.company h2{text-align:center;font-size:13px;font-weight:500;letter-spacing:.1em}
.company table{width:520px;margin:18px auto 0;border-collapse:collapse;font-size:10px}
.company th,.company td{border-bottom:1px solid var(--line);padding:5px 10px;text-align:left;font-weight:400}
.company th{width:180px;color:var(--muted)}
.company .cat-mark{position:absolute;right:150px;top:220px;width:50px;height:70px;background:var(--orange);border-radius:20px 20px 6px 6px}

/* footer */
.site-footer{top:4080px;height:112px;background:var(--dark);color:var(--white);display:flex;align-items:center;justify-content:space-between;padding:0 160px}
.site-footer .logo{color:var(--white);font-size:26px}
.site-footer .logo small{color:#bbb}
.site-footer .links{font-size:10px;color:#bbb;line-height:1.8}
.site-footer .copy{font-size:9px;color:#999;align-self:flex-end;padding-bottom:12px}
</style>
</head>
<body>
<div class="page">

<header class="site-header">
  <div class="logo">猫ごよみ</div>
  <div class="sns-mini"><span></span><span></span></div>
</header>

<nav class="global-nav">
  <ul><li>TOP</li><li>店内の様子</li><li>猫紹介</li><li>システム</li><li>Q&amp;A</li><li>ルール</li><li>SNS</li></ul>
</nav>

<section class="hero">
  <div class="photo" role="img" aria-label="横たわってこちらを見つめる猫の写真"></div>
  <div class="badge">2015.5.30<br>OPEN予定!!</div>
  <div class="title">
    <div class="logo">猫ごよみ</div>
    <em>neko goyomi</em>
  </div>
  <p class="lead">～ 猫と過ごす癒しの空間 ～<br>アキバの猫と触れ合い処</p>
</section>

<section class="concept">
  <h2 class="sec-title">猫ごよみのコンセプト</h2>
  <div class="thumbs">
    <span class="ph" role="img" aria-label="カウンターでくつろぐ猫の写真" style="background:linear-gradient(135deg,#b9a68f,#ece3d6)"></span>
    <span class="ph" role="img" aria-label="眠る猫の写真" style="background:linear-gradient(135deg,#8a8a8a,#d8d2ca)"></span>
    <span class="ph" role="img" aria-label="猫と遊ぶお客様の写真" style="background:linear-gradient(135deg,#d9c4a6,#8f7f6d)"></span>
    <span class="ph" role="img" aria-label="窓辺の猫の写真" style="background:linear-gradient(135deg,#cfc4b4,#7d7468)"></span>
  </div>
</section>

<section class="intro" role="img" aria-label="ぼかした店内の背景写真">
  <h2>はじめに</h2>
  <p>都会の喧騒を忘れて、猫たちとゆったりした時間をお過ごしください。</p>
</section>

<section class="shop">
  <h2 class="sec-title">店内の様子</h2>
  <div class="gallery">
    <span class="ph" role="img" aria-label="店内の写真" style="left:0;top:60px;width:90px;height:70px;background:linear-gradient(135deg,#c69a6a,#7a5a3c)"></span>
    <span class="ph" role="img" aria-label="キャットタワーの写真" style="left:100px;top:50px;width:90px;height:80px;background:linear-gradient(135deg,#b89d7c,#e4d6c2)"></span>
    <span class="ph" role="img" aria-label="店内全体の写真" style="left:200px;top:0;width:160px;height:190px;background:linear-gradient(160deg,#a88a62,#e0cfa8 60%,#9a7b55)"></span>
    <span class="ph" role="img" aria-label="くつろぎスペースの写真" style="left:370px;top:50px;width:90px;height:80px;background:linear-gradient(135deg,#d8c8b0,#8c7658)"></span>
    <span class="ph" role="img" aria-label="ソファ席の写真" style="left:470px;top:60px;width:90px;height:70px;background:linear-gradient(135deg,#b07a4e,#e6c9a4)"></span>
  </div>
</section>

<section class="cats">
  <h2 class="sec-title">猫紹介</h2>
  <div class="cat-list">
    <div class="cat-card"><span class="ph" role="img" aria-label="三毛猫の写真" style="background:linear-gradient(135deg,#e9e3da,#b58d62)"></span><p>ミケ</p></div>
    <div class="cat-card"><span class="ph" role="img" aria-label="白黒猫の写真" style="background:linear-gradient(135deg,#d9d4cc,#5a5550)"></span><p>ココ</p></div>
    <div class="cat-card"><span class="ph" role="img" aria-label="茶白猫の写真" style="background:linear-gradient(135deg,#e2b07a,#f1e6d6)"></span><p>ソラ</p></div>
    <div class="cat-card"><span class="ph" role="img" aria-label="長毛の白猫の写真" style="background:linear-gradient(135deg,#f2ece4,#c9b89f)"></span><p>ルナ</p></div>
  </div>
</section>

<section class="system">
  <h2 class="sec-title">システム</h2>
  <div class="price-list">
    <div class="price"><strong><b>10</b>分 <b>200</b>円<small>(税抜)</small></strong><span>以降10分ごとに200円の延長料金がかかります</span></div>
    <div class="price"><strong>ドリンクバー 350円<small>(税抜)</small></strong><span>お好きなドリンクを何杯でもお楽しみいただけます</span></div>
    <div class="price snack"><strong>猫のおやつ 500円<small>(税抜)</small></strong><span>猫たちにおやつをあげることができます</span></div>
    <div class="price hours"><strong>営業時間 <b>10時〜20時</b></strong><span>最終入店は19時30分まで・年中無休</span></div>
  </div>
  <p class="note">料金はすべて税抜表示となっております。</p>
</section>

<section class="qa">
  <h2 class="sec-title">Q&amp;A</h2>
  <div class="qa-list">
    <div class="qa-item">
      <h3>Q. 猫カフェは予約が必要ですか？</h3>
      <p>A. 予約は不要です。<br>混雑時はお待ちいただく場合がございます。<br>お気軽にご来店ください。</p>
    </div>
    <div class="qa-item">
      <h3>Q. 猫を抱っこしてもいいですか？</h3>
      <p>A. 無理な抱っこはご遠慮ください。<br>猫が自分から近づいてきた時は、やさしく撫でてあげてください。<br>スタッフがお手伝いいたします。</p>
    </div>
  </div>
  <span class="qa-more">質問をもっと見る</span>
</section>

<section class="rules">
  <div class="rules-board">
    <h2 class="sec-title">ルール</h2>
    <div class="rule-grid">
      <div class="rule-intro"><span class="ph" role="img" aria-label="猫のイラスト" style="background:var(--orange-soft)"></span>猫ちゃんと<br>楽しく遊ぶために<br>守って欲しいこと</div>
      <div class="rule-card ng" style="left:150px;top:0"><span class="ph" role="img" aria-label="追いかけられる猫のイラスト" style="background:linear-gradient(135deg,#e6e0d8,#c9bfb2)"></span>追いかけない！</div>
      <div class="rule-card ng" style="left:300px;top:0"><span class="ph" role="img" aria-label="起こされる猫のイラスト" style="background:linear-gradient(135deg,#ede4d6,#cdb9a0)"></span>起こさないで！</div>
      <div class="rule-card ng" style="left:150px;top:160px"><span class="ph" role="img" aria-label="食べ物と猫のイラスト" style="background:linear-gradient(135deg,#efe6d8,#c9b49a)"></span>食べ物の持ち込みNG</div>
      <div class="rule-card ng" style="left:300px;top:160px"><span class="ph" role="img" aria-label="カメラと猫のイラスト" style="background:linear-gradient(135deg,#e8e4de,#bdb3a6)"></span>フラッシュはNG</div>
      <div class="rule-card ng" style="left:450px;top:160px"><span class="ph" role="img" aria-label="大声に驚く猫のイラスト" style="background:linear-gradient(135deg,#ede6dc,#c4b6a3)"></span>大きな声はNG</div>
    </div>
  </div>
  <div class="rules-text">
    <p>その他、猫の健康を守るためにも以下の点にご協力をお願いいたします。店内では手洗いと消毒をお願いしております。</p>
    <p>こちらのルールは猫ちゃんとお客様が安心して過ごしていただくためのものです。</p>
    <p>小学生以下のお子様は保護者の方とご一緒にご来店ください。</p>
    <p>ペット連れでのご入店はご遠慮ください。</p>
    <p>猫に怪我をさせてしまった場合や、猫によってお客様の持ち物が破損した場合の補償は致しかねますので予めご了承ください。</p>
  </div>
</section>

<section class="access">
  <h2 class="sec-title">アクセス</h2>
  <div class="access-body">
    <div class="access-info">
      <div class="logo">猫ごよみ <small>秋葉原店</small></div>
      <address>東京都千代田区外神田9-9-9 にゃんビル2F</address>
      <span class="ph" role="img" aria-label="階段に座る猫の写真" style="background:linear-gradient(135deg,#d8d4ce,#7d7770)"></span>
    </div>
    <span class="ph map" role="img" aria-label="店舗周辺の地図" style="background:linear-gradient(135deg,#eceae4,#d9d6cf)"></span>
  </div>
</section>

<section class="sns">
  <h2 class="sec-title">SNS</h2>
  <div class="sns-list">
    <div class="sns-card"><div class="inner">猫ごよみ 公式ページ<span class="ph" role="img" aria-label="店内の写真" style="background:linear-gradient(135deg,#c9a27a,#efe1cc)"></span>新しい仲間が増えました。ぜひ会いに来てください。</div></div>
    <div class="sns-card"><div class="inner">猫ごよみ 公式アカウント<span class="ph" role="img" aria-label="猫の写真" style="background:linear-gradient(135deg,#b9b1a6,#e8e2d8)"></span>本日も元気に営業中です。お待ちしております。</div></div>
    <div class="sns-card talk"><div class="inner"><div class="tag">トーク</div><div class="logo">猫ごよみ</div><div class="sub">neko goyomi</div><p>友だち追加でお得な<br>クーポン配信中!!</p></div></div>
  </div>
</section>

<section class="company">
  <h2>猫ごよみ 会社概要</h2>
  <table>
    <tr><th>社名</th><td>株式会社ねこごよみ</td></tr>
    <tr><th>代表取締役</th><td>代表 猫山太郎</td></tr>
    <tr><th>所在地</th><td>東京都千代田区外神田9-9-9</td></tr>
    <tr><th>第一種動物取扱業</th><td>登録済み</td></tr>
    <tr><th>事業所の名称</th><td>猫ごよみ 秋葉原店</td></tr>
    <tr><th>登録番号</th><td>第000000号</td></tr>
    <tr><th>登録年月日</th><td>平成27年4月1日</td></tr>
    <tr><th>有効期間</th><td>平成32年3月31日まで</td></tr>
    <tr><th>動物取扱責任者</th><td>猫山花子</td></tr>
  </table>
  <span class="cat-mark" role="img" aria-label="座る猫のシルエット"></span>
</section>

<footer class="site-footer">
  <div class="logo">猫ごよみ <small>neko goyomi</small></div>
  <div class="links">ABOUT US<br>お問い合わせ<br>プライバシーポリシー</div>
  <div class="copy">© neko goyomi</div>
</footer>

</div>
</body>
</html>
```